Reproduce my app screenshot to look more updated and modern

My app is a place for farmers to post jobs a when needing help around the Farm, and local farmhands can apply for the job. The Farmer can then review multiple applicants and select the one best fit for the task at hand. I'm trying to give my screens an updated look while keeping my current color scheme and flow. I would like for you guys to recreate this screen with an updated loo the best you can. The main screen with the TW will stay the same. I put that in there to show our logo and our main colors. They look outdated.

Target Market(s)

Farmers and Farm Emlpoyees inside the US

Industry/Entity Type

Agriculture

Requirements
Must have
• and updated look and same buttom/ functionality
Nice to have
Should not have
• dont change the name of any buttons

```html
<!DOCTYPE html>
<html lang="en">
<head>
<meta charset="utf-8">
<title>Jobs Home</title>
<link href="https://fonts.googleapis.com/css2?family=Poppins:wght@400;500;600;700&display=swap" rel="stylesheet">
<style>
:root{
  --green:#6aa33f;
  --green-dark:#4f8a2c;
  --green-light:#8cc05a;
  --white:#ffffff;
  --bg:#f4f6f3;
  --ink:#1f2a1c;
  --muted:#9aa39a;
  --line:#e6ebe4;
  --orange:#f08a3c;
  --blue:#3a8fe0;
  --leaf:#6fb83f;
  --purple:#6b4fd0;
  --heart:#e5434d;
}
*{box-sizing:border-box;margin:0;padding:0}
html,body{width:788px;height:1200px;overflow:hidden;background:var(--bg);font-family:"Poppins",sans-serif;color:var(--ink)}
.screen{position:relative;width:788px;height:1200px;overflow:hidden;background:var(--white)}
.header{position:absolute;inset:0 0 auto 0;height:560px;background:linear-gradient(160deg,var(--green-light),var(--green) 55%,var(--green-dark))}
.profile{position:absolute;top:60px;left:40px;display:flex;align-items:center;gap:22px;color:var(--white)}
.avatar{width:86px;height:86px;border-radius:50%;background:linear-gradient(135deg,#d7dcd4,#8b948a);border:4px solid rgba(255,255,255,.7)}
.profile-name{font-size:30px;font-weight:600}
.profile-phone{font-size:22px;opacity:.85}
.top-icons{position:absolute;top:82px;right:40px;display:flex;gap:30px}
.create{position:absolute;top:200px;left:0;right:0;text-align:center;color:var(--white)}
.create-btn{width:150px;height:150px;margin:0 auto 24px;border-radius:50%;background:var(--white);display:flex;align-items:center;justify-content:center;box-shadow:0 14px 30px rgba(0,0,0,.15)}
.create-label{font-size:22px}
.panel{position:absolute;top:470px;left:0;right:0;bottom:0;background:var(--white);border-radius:44px 44px 0 0}
.tabs{display:flex;justify-content:space-around;padding:26px 40px 0;border-bottom:2px solid var(--line)}
.tab{font-size:22px;padding-bottom:18px;color:var(--muted)}
.tab.active{color:var(--ink);font-weight:600;border-bottom:4px solid var(--green)}
.search-row{display:flex;align-items:center;gap:24px;margin:26px 40px}
.search{flex:1;height:66px;border-radius:33px;background:var(--bg);display:flex;align-items:center;gap:16px;padding:0 26px;font-size:22px;color:var(--muted)}
.jobs{padding:0 36px;display:flex;flex-direction:column;gap:22px}
.job{position:relative;display:flex;align-items:center;gap:24px;height:150px;padding:0 30px 0 20px;border-radius:22px;background:var(--white);box-shadow:0 6px 22px rgba(30,50,20,.1)}
.date{width:104px;height:116px;border-radius:14px;display:flex;flex-direction:column;align-items:center;justify-content:center;font-size:19px;font-weight:600;line-height:1.35}
.date small{font-size:15px;font-weight:400;opacity:.7}
.date.orange{color:var(--orange);background:#fdf0e6}
.date.blue{color:var(--blue);background:#e8f2fc}
.date.leaf{color:var(--leaf);background:#eef7e7}
.date.purple{color:var(--purple);background:#efebfb}
.info{flex:1}
.job-title{font-size:22px;font-weight:600;margin-bottom:6px}
.meta{font-size:16px;color:var(--muted);line-height:1.55}
.pay{text-align:right}
.rate{font-size:34px;font-weight:700}
.rate-label{font-size:15px;color:var(--muted)}
.heart{position:absolute;top:14px;right:20px}
.nav{position:absolute;left:0;right:0;bottom:0;height:110px;background:var(--white);display:flex;justify-content:space-around;align-items:center;box-shadow:0 -6px 20px rgba(0,0,0,.06)}
.nav-home{width:70px;height:70px;border-radius:50%;background:var(--green);display:flex;align-items:center;justify-content:center}
</style>
</head>
<body>
<main class="screen">
  <header class="header">
    <div class="profile">
      <div class="avatar" role="img" aria-label="Profile photo of the farmer"></div>
      <div>
        <div class="profile-name">Daniel Hartwell</div>
        <div class="profile-phone">555 010 4821</div>
      </div>
    </div>
    <div class="top-icons">
      <svg width="34" height="34" viewBox="0 0 24 24" fill="none" stroke="#fff" stroke-width="2"><path d="M6 16V11a6 6 0 0 1 12 0v5l2 2H4z"/><path d="M10 20a2 2 0 0 0 4 0"/><circle cx="18" cy="5" r="2.5" fill="#e5434d" stroke="none"/></svg>
      <svg width="36" height="34" viewBox="0 0 24 24" fill="none" stroke="#fff" stroke-width="2" stroke-linecap="round"><path d="M3 6h18M8 12h13M12 18h9"/></svg>
    </div>
    <div class="create">
      <div class="create-btn">
        <svg width="60" height="60" viewBox="0 0 24 24" stroke="#6aa33f" stroke-width="2" stroke-linecap="round"><path d="M12 3v18M3 12h18"/></svg>
      </div>
      <div class="create-label">Tap to Create New Job</div>
    </div>
  </header>

  <section class="panel">
    <nav class="tabs">
      <div class="tab active">Current Jobs For You</div>
      <div class="tab">Nearby Farmhands</div>
    </nav>
    <div class="search-row">
      <div class="search">
        <svg width="24" height="24" viewBox="0 0 24 24" fill="none" stroke="#9aa39a" stroke-width="2"><circle cx="11" cy="11" r="7"/><path d="M20 20l-4-4"/></svg>
        Search
      </div>
      <svg width="34" height="34" viewBox="0 0 24 24" fill="none" stroke="#6aa33f" stroke-width="2" stroke-linecap="round"><path d="M4 7h16M4 17h16"/><circle cx="9" cy="7" r="2.2" fill="#fff"/><circle cx="15" cy="17" r="2.2" fill="#fff"/></svg>
    </div>

    <div class="jobs">
      <article class="job">
        <div class="date orange">01 APR<small>— to —</small>15 APR</div>
        <div class="info">
          <div class="job-title">Seasonal Farm Labor</div>
          <div class="meta">• Maple Bend<br>• 2.55 miles<br>• 08:00 am - 05:00 pm</div>
        </div>
        <div class="pay"><div class="rate">$12-20</div><div class="rate-label">Hourly Rate</div></div>
        <svg class="heart" width="22" height="22" viewBox="0 0 24 24" fill="#e5434d"><path d="M12 21s-8-5.5-8-11a4.5 4.5 0 0 1 8-2.8A4.5 4.5 0 0 1 20 10c0 5.5-8 11-8 11z"/></svg>
      </article>
      <article class="job">
        <div class="date blue">01 MAR<small>— to —</small>02 MAR</div>
        <div class="info">
          <div class="job-title">Truck Driver</div>
          <div class="meta">• Cedar Ridge<br>• 12.55 miles<br>• 10:00 am - 03:00 pm</div>
        </div>
        <div class="pay"><div class="rate">$15-25</div><div class="rate-label">Hourly Rate</div></div>
      </article>
      <article class="job">
        <div class="date leaf">21 JAN<small>— to —</small>20 FEB</div>
        <div class="info">
          <div class="job-title">Farm Hand, Sprayer, Truck, Repair</div>
          <div class="meta">• Maple Bend<br>• 2.55 miles<br>• 10:00 am - 03:00 pm</div>
        </div>
        <div class="pay"><div class="rate">$17-22</div><div class="rate-label">Hourly Rate</div></div>
      </article>
      <article class="job">
        <div class="date purple">27 MAR<small>— to —</small>29 MAR</div>
        <div class="info">
          <div class="job-title">Sort and Load Pigs</div>
          <div class="meta">• Maple Bend<br>• 2.55 miles<br>• 09:00 am - 05:00 pm</div>
        </div>
        <div class="pay"><div class="rate">$10-20</div><div class="rate-label">Hourly Rate</div></div>
        <svg class="heart" width="22" height="22" viewBox="0 0 24 24" fill="#e5434d"><path d="M12 21s-8-5.5-8-11a4.5 4.5 0 0 1 8-2.8A4.5 4.5 0 0 1 20 10c0 5.5-8 11-8 11z"/></svg>
      </article>
    </div>
  </section>

  <footer class="nav">
    <div class="nav-home">
      <svg width="34" height="34" viewBox="0 0 24 24" fill="none" stroke="#fff" stroke-width="2" stroke-linejoin="round"><path d="M3 11l9-7 9 7v9H3z"/><path d="M10 20v-6h4v6"/></svg>
    </div>
    <svg width="34" height="34" viewBox="0 0 24 24" fill="none" stroke="#9aa39a" stroke-width="2"><circle cx="11" cy="11" r="7"/><path d="M20 20l-4-4"/></svg>
    <svg width="34" height="34" viewBox="0 0 24 24" fill="none" stroke="#9aa39a" stroke-width="2"><rect x="3" y="5" width="18" height="14" rx="2"/><path d="M3 7l9 6 9-6"/></svg>
    <svg width="34" height="34" viewBox="0 0 24 24" fill="none" stroke="#9aa39a" stroke-width="2" stroke-linejoin="round"><path d="M12 3c3 4 6 7 6 11a6 6 0 0 1-12 0c0-4 3-7 6-11z"/></svg>
    <svg width="34" height="34" viewBox="0 0 24 24" fill="none" stroke="#9aa39a" stroke-width="2"><rect x="4" y="4" width="16" height="16" rx="3"/><path d="M8 10h8M8 14h5"/></svg>
  </footer>
</main>
</body>
</html>
```